Tidewind Coves Boat Business Website

I would like a website that looks fresh, fun and exciting with great colors and photos of people having fun sailing and power boating. Current web page is www.tidewindcoves.example. I want to be able to change content and photos myself once completed. Also needs to have customized info request forms and access to enrollment forms. Should work across all browsers and platforms including iPad and Mac. I have three product lines...instruction, charters and trips. See also keelhour.example/new-york, and facebook.com/tidewindcoves, /keelhournewyork and /coralpalmlounge.

Reason: We are reviewing the designs submitted and will provide feedback asap. Thank you.

Industry/Entity Type

Business

Requirements
Must have
• self management/content management
form submissions
color, fun, excitement
links pages
photo pages
Nice to have
• calendar/class scheduling
guest book
visitor uploadable photos

```html
<!DOCTYPE html>
<html lang="en">
<head>
<meta charset="utf-8">
<title>Tidewind Coves Charter Co. &amp; Nautical School</title>
<link rel="stylesheet" href="https://fonts.googleapis.com/css2?family=Open+Sans:wght@400;600;700&family=Didact+Gothic&display=swap">
<style>
:root{
  --teal:#1aa6a0;
  --ink:#2b2b2b;
  --text:#555;
  --orange:#f7a800;
  --btn-blue:#0d5fa0;
  --navy:#103e66;
  --bar-top:#4a4a4a;
  --bar-bottom:#2a2a2a;
  --footer:#3a3a3a;
  --caption-bg:#f0f0f0;
  --rule:#d6d6d6;
  --hero-sky:#dfe7ec;
  --hero-glow:#f6deaa;
  --hero-sea:#4d7699;
}
*{box-sizing:border-box;margin:0;padding:0}
html,body{width:1079px;height:1200px;overflow:hidden;background:#fff}
body{font-family:"Open Sans",sans-serif;color:var(--text)}
.page{position:relative;width:1079px;height:1200px;overflow:hidden}

/* header */
.site-header{position:absolute;left:0;top:0;width:1079px;height:99px;background:#fff}
.brand{position:absolute;left:108px;top:38px}
.brand-name{font-family:"Didact Gothic",sans-serif;font-size:28px;color:var(--teal);letter-spacing:.5px;white-space:nowrap}
.main-nav{position:absolute;top:58px;left:0;width:1079px;font-size:12px;color:var(--ink)}
.main-nav a{position:absolute;color:inherit;text-decoration:none;white-space:nowrap}
.main-nav a.active{color:var(--teal);font-weight:600}

/* hero */
.hero{position:absolute;left:0;top:99px;width:1079px;height:348px;
  background:linear-gradient(100deg,var(--hero-sky) 0%,#c9d3da 35%,var(--hero-glow) 62%,#f3e2bc 85%,#e9dcc2 100%)}
.hero::after{content:"";position:absolute;left:0;right:0;bottom:0;height:120px;
  background:linear-gradient(180deg,rgba(77,118,153,0) 0%,rgba(77,118,153,.55) 60%,var(--hero-sea) 100%)}
.hero-title{position:absolute;z-index:1;left:632px;top:131px;font-family:"Didact Gothic",sans-serif;font-weight:400;font-size:27px;line-height:31px;letter-spacing:2px;color:#222}
.btn-read{position:absolute;z-index:1;left:634px;top:234px;width:95px;height:30px;background:var(--orange);color:#222;font-size:12px;font-weight:600;display:flex;align-items:center;justify-content:center;border-radius:2px}
.slider-dots{position:absolute;z-index:1;left:751px;top:244px;display:flex;gap:5px}
.slider-dots span{width:9px;height:9px;border-radius:50%;background:#111}
.slider-dots span.on{background:#1e6fa5}

/* feature bar */
.feature-bar{position:absolute;left:0;top:447px;width:1079px;height:84px;background:linear-gradient(180deg,var(--bar-top),var(--bar-bottom))}
.feature{position:absolute;top:16px;display:flex;gap:10px;color:#fff}
.feature-icon{width:47px;height:47px;border-radius:6px;background:linear-gradient(180deg,#fff,#d8d8d8);display:flex;align-items:center;justify-content:center}
.feature h3{font-size:12px;font-weight:600;margin-top:2px}
.feature p{font-size:10px;line-height:14px;margin-top:4px;color:#eee}

/* welcome */
.section-title{font-size:18px;font-weight:400;color:var(--ink)}
.welcome-title{position:absolute;left:111px;top:561px}
.welcome-rule{position:absolute;left:111px;top:588px;width:628px;height:1px;background:var(--rule)}
.welcome-text{position:absolute;left:116px;top:594px;width:620px;font-size:11px;line-height:21px}
.product{position:absolute;top:689px;width:196px}
.product-frame{height:111px;border:1px solid #c7c7c7;border-radius:4px;padding:5px;background:#fff}
.product-photo{position:relative;height:99px;border-radius:2px}
.product-label{position:absolute;left:0;bottom:0;width:100%;height:20px;background:rgba(0,0,0,.6);color:#fff;font-size:13px;line-height:20px;padding-left:5px}
.product p{font-size:11px;line-height:14px;margin:11px 3px 0;color:var(--text)}
.btn-more{display:inline-flex;align-items:center;gap:4px;margin:9px 0 0 3px;height:21px;padding:0 8px;background:var(--btn-blue);color:#fff;font-size:10px;font-weight:600;border-radius:2px}

/* calendar */
.calendar-title{position:absolute;left:752px;top:561px}
.calendar-sub{position:absolute;left:760px;top:586px;font-size:13px;color:var(--ink)}
.calendar{position:absolute;left:758px;top:629px;width:208px;background:#fff;box-shadow:0 3px 8px rgba(0,0,0,.25)}
.cal-head{position:relative;height:36px;background:linear-gradient(180deg,#ffb400,#f59c00);display:flex;align-items:center;justify-content:center;font-size:15px;font-weight:600;color:#1a1a1a}
.cal-head .arrow{position:absolute;top:13px;width:0;height:0;border-top:4px solid transparent;border-bottom:4px solid transparent}
.cal-head .prev{left:33px;border-right:5px solid #fff}
.cal-head .next{right:33px;border-left:5px solid #fff}
.ring{position:absolute;top:-11px;width:4px;height:20px;border:1px solid #777;border-radius:2px;background:#eee}
.cal-grid{display:grid;grid-template-columns:repeat(7,1fr);background:#f2f2f2}
.cal-grid .dow{font-size:8px;text-align:center;padding:4px 0;color:#777;border-bottom:1px solid #ddd}
.cal-grid .d{position:relative;height:29.7px;font-size:12px;font-weight:600;color:#555;display:flex;align-items:center;justify-content:center;border-right:1px solid #e2e2e2;border-bottom:1px solid #e2e2e2;background:#f7f7f7}
.cal-grid .d.muted{color:#bbb}
.cal-grid .d.today{background:var(--orange);color:#111}
.cal-grid .d.sel{background:#e2e2e2}
.ev{position:absolute;bottom:4px;left:50%;display:flex;gap:2px;transform:translateX(-50%)}
.ev i{width:4px;height:4px;border-radius:50%}
.ev .b{background:#3b87c8}.ev .o{background:var(--orange)}.ev .w{background:#fff}
.guestbook{position:absolute;left:760px;top:857px;font-size:16px;font-weight:700;color:var(--navy);letter-spacing:-.5px}

/* gallery */
.gallery-title{position:absolute;left:114px;top:917px}
.gal-arrow{position:absolute;top:916px;width:22px;height:22px;border-radius:50%;border:1px solid #555;background:linear-gradient(180deg,#fff,#ccc);display:flex;align-items:center;justify-content:center}
.gal-item{position:absolute;top:948px;width:199px}
.gal-photo{height:140px}
.gal-caption{height:36px;background:var(--caption-bg);text-align:center;font-size:13px;line-height:36px;color:#666}
.gal-item.active .gal-caption{border-bottom:3px solid var(--orange);height:35px;line-height:34px}

/* footer */
.site-footer{position:absolute;left:0;top:1155px;width:1079px;height:45px;background:var(--footer)}
.site-footer p{position:absolute;left:117px;top:15px;font-size:10px;color:#fff;font-weight:600}
.social{position:absolute;top:12px;width:21px;height:21px;border-radius:50%}
</style>
</head>
<body>
<div class="page">

  <header class="site-header">
    <div class="brand"><span class="brand-name">Tidewind Coves</span></div>
    <nav class="main-nav">
      <a class="active" style="left:415px">HOME</a>
      <a style="left:477px">Nautical School</a>
      <a style="left:586px">Charter Sailing</a>
      <a style="left:691px">Our Captains</a>
      <a style="left:788px">Adventure Travels</a>
      <a style="left:912px">Contact Us</a>
    </nav>
  </header>

  <section class="hero" role="img" aria-label="Photo: sailboat heeling under sail across open water at sunset">
    <h1 class="hero-title">“THE WORLD'S LARGEST<br>FRACTIONAL BOATING<br>COMPANY ”</h1>
    <div class="btn-read">READ MORE</div>
    <div class="slider-dots"><span></span><span class="on"></span><span></span></div>
  </section>

  <section class="feature-bar">
    <div class="feature" style="left:111px">
      <div class="feature-icon"><svg width="26" height="24" viewBox="0 0 26 24"><path d="M12 2 L12 16 L4 16 Z" fill="#1e6fa5"/><path d="M14 5 L14 16 L21 16 Z" fill="#1e6fa5"/><path d="M3 18 H23 L20 22 H6 Z" fill="#1e6fa5"/></svg></div>
      <div><h3>Nautical School</h3><p>Lorem ipsum dolor sit amet<br>consectetur adipscing elit.</p></div>
    </div>
    <div class="feature" style="left:336px">
      <div class="feature-icon"><span style="font-size:30px;font-weight:700;color:#1e6fa5;line-height:1">$</span></div>
      <div><h3>Charter Sailing</h3><p>Lorem ipsum dolor sit amet<br>consectetur adipscing elit.</p></div>
    </div>
    <div class="feature" style="left:561px">
      <div class="feature-icon"><svg width="28" height="28" viewBox="0 0 28 28"><circle cx="14" cy="14" r="11" fill="none" stroke="#1e6fa5" stroke-width="3"/><path d="M19 9 L15.5 15.5 L9 19 L12.5 12.5 Z" fill="#1e6fa5"/></svg></div>
      <div><h3>Adventure Travel</h3><p>Lorem ipsum dolor sit amet<br>consectetur adipscing elit.</p></div>
    </div>
    <div class="feature" style="left:786px">
      <div class="feature-icon"><svg width="28" height="26" viewBox="0 0 28 26"><path d="M14 2 L22 11 H17 V18 H11 V11 H6 Z" fill="#1e6fa5"/><path d="M3 16 V23 H25 V16" fill="none" stroke="#1e6fa5" stroke-width="3"/></svg></div>
      <div><h3>Upload Your Photos</h3><p>Lorem ipsum dolor sit amet<br>consectetur adipscing elit.</p></div>
    </div>
  </section>

  <h2 class="section-title welcome-title">Welcome To Tidewind Coves</h2>
  <div class="welcome-rule"></div>
  <p class="welcome-text">Lorem Ipsum is simply dummy text of the printing and typesetting industry. Lorem Ipsum has been the industry's standard dummy text ever since the 1500s, when an unknown printer took a galley of type and scrambled it to make a type specimen book. It has survived not only five centuries, but also the leap into electronic typesetting, remaining essentially unchanged.</p>

  <article class="product" style="left:113px">
    <div class="product-frame"><div class="product-photo" role="img" aria-label="Photo: instructor teaching students at the helm of a sailboat" style="background:linear-gradient(180deg,#6fa3d6,#3d5f86 60%,#2a3550)"><span class="product-label">Instructions</span></div></div>
    <p>Lorem Ipsum is simply dummy text of the printing and typesetting industry.</p>
    <span class="btn-more">Read More <svg width="8" height="7" viewBox="0 0 8 7"><path d="M0 0 L3 3.5 L0 7 M4 0 L7 3.5 L4 7" fill="none" stroke="#fff" stroke-width="1.3"/></svg></span>
  </article>
  <article class="product" style="left:323px">
    <div class="product-frame"><div class="product-photo" role="img" aria-label="Photo: motor yacht cruising on calm water" style="background:linear-gradient(180deg,#8aa4b8,#6f8ca3 55%,#3f5f7c)"><span class="product-label">Charters</span></div></div>
    <p>Lorem Ipsum is simply dummy text of the printing and typesetting industry.</p>
    <span class="btn-more">Read More <svg width="8" height="7" viewBox="0 0 8 7"><path d="M0 0 L3 3.5 L0 7 M4 0 L7 3.5 L4 7" fill="none" stroke="#fff" stroke-width="1.3"/></svg></span>
  </article>
  <article class="product" style="left:532px">
    <div class="product-frame"><div class="product-photo" role="img" aria-label="Photo: group riding an inflatable speedboat across the waves" style="background:linear-gradient(180deg,#a9c4dc,#5f86b0 55%,#2c4f80)"><span class="product-label">Trips</span></div></div>
    <p>Lorem Ipsum is simply dummy text of the printing and typesetting industry.</p>
    <span class="btn-more">Read More <svg width="8" height="7" viewBox="0 0 8 7"><path d="M0 0 L3 3.5 L0 7 M4 0 L7 3.5 L4 7" fill="none" stroke="#fff" stroke-width="1.3"/></svg></span>
  </article>

  <h2 class="section-title calendar-title">Calendar Tidewind Coves</h2>
  <p class="calendar-sub">(Update Tidewind Coves Events)</p>
  <div class="calendar">
    <span class="ring" style="left:18px"></span><span class="ring" style="right:18px"></span>
    <div class="cal-head"><span class="arrow prev"></span>January 2013<span class="arrow next"></span></div>
    <div class="cal-grid">
      <div class="dow">SUN</div><div class="dow">MON</div><div class="dow">TUE</div><div class="dow">WED</div><div class="dow">THU</div><div class="dow">FRI</div><div class="dow">SAT</div>
      <div class="d muted">30</div><div class="d">1<span class="ev"><i class="b"></i></span></div><div class="d">2</div><div class="d">3</div><div class="d">4</div><div class="d">5<span class="ev"><i class="o"></i></span></div><div class="d">7</div>
      <div class="d">8</div><div class="d">9</div><div class="d today">10<span class="ev"><i class="w"></i></span></div><div class="d">11<span class="ev"><i class="o"></i></span></div><div class="d">12</div><div class="d">13</div><div class="d">14</div>
      <div class="d">15</div><div class="d">16</div><div class="d">17</div><div class="d">18</div><div class="d">19</div><div class="d sel">20<span class="ev"><i class="o"></i></span></div><div class="d">21</div>
      <div class="d">22<span class="ev"><i class="b"></i></span></div><div class="d">23</div><div class="d">24</div><div class="d">25<span class="ev"><i class="b"></i><i class="o"></i></span></div><div class="d">26</div><div class="d">27</div><div class="d">28</div>
      <div class="d">29</div><div class="d">30</div><div class="d">31</div><div class="d muted">1</div><div class="d muted">2</div><div class="d muted">3</div><div class="d muted">4</div>
    </div>
  </div>
  <a class="guestbook">Click Here to see guest book</a>

  <h2 class="section-title gallery-title">Photo Gallery</h2>
  <span class="gal-arrow" style="left:910px"><svg width="8" height="9" viewBox="0 0 8 9"><path d="M1 0 L7 4.5 L1 9 Z" fill="#222"/></svg></span>
  <span class="gal-arrow" style="left:943px"><svg width="8" height="9" viewBox="0 0 8 9"><path d="M7 0 L1 4.5 L7 9 Z" fill="#222"/></svg></span>

  <figure class="gal-item" style="left:114px">
    <div class="gal-photo" role="img" aria-label="Photo: friends relaxing on the deck of a sailboat" style="background:linear-gradient(180deg,#c5ccd2,#a58f78 60%,#7a5a44)"></div>
    <figcaption class="gal-caption">Lorem Ipsum</figcaption>
  </figure>
  <figure class="gal-item active" style="left:330px">
    <div class="gal-photo" role="img" aria-label="Photo: group laughing together in a boat cockpit" style="background:linear-gradient(180deg,#3a3a3a,#6a6258 55%,#9c8a70)"></div>
    <figcaption class="gal-caption">Lorem Ipsum</figcaption>
  </figure>
  <figure class="gal-item" style="left:547px">
    <div class="gal-photo" role="img" aria-label="Photo: family fishing from the back of a motorboat" style="background:linear-gradient(180deg,#9cb0a8,#dfe5ea 55%,#4a6e98)"></div>
    <figcaption class="gal-caption">Lorem Ipsum</figcaption>
  </figure>
  <figure class="gal-item" style="left:765px">
    <div class="gal-photo" role="img" aria-label="Photo: crew in bright jackets sailing a small keelboat" style="background:linear-gradient(180deg,#dfe6ea,#8fb0cc 55%,#3d6e9c)"></div>
    <figcaption class="gal-caption">Lorem Ipsum</figcaption>
  </figure>

  <footer class="site-footer">
    <p>©copyright 2013. Tidewind Coves Charter Co. and Nautical School. All rights reserved.</p>
    <span class="social" style="left:846px;background:#3fb4e6"></span>
    <span class="social" style="left:874px;background:#3b5ea8"></span>
    <span class="social" style="left:902px;background:#666"></span>
    <span class="social" style="left:930px;background:#1e77b5"></span>
  </footer>

</div>
</body>
</html>
```